We invest in Electric Vehicles and renewable energy - help sell us!

INTRO: We want a PowerPoint template / Master Presentation to be used to sell our company and first investment fund to professional investors and to present ourselves to businesses that will develop the infrastructure projects in which we will invest.

WHO WE ARE: We are a newly created investment advisory and fund management company specialised in sustainable mobility.

WHAT WE DO: We invest in infrastructure projects that provide electric vehicles, charging infrastructure (charging stations etc) and associated renewable energy generation services (eg solar panels on roof-tops and solar parks, wind energy). The users of the projects in which we invest are operators of vehicle fleets (taxis, buses, delivery, which may be for 2, 3 and 4 wheel vehicles from motorbikes through cars, vans, buses and trucks).

PURPOSE OF THE POWERPOINT: We are looking for a presentation (1) to sell our investment services to investors (to raise money) and (2) to present what we do to fleet operators and service providers who will develop the projects.

CONTENT: We need all of the usual front cover slide / content slide / intermediate divider-heading slide / slides that integrate the most common tables, charts and smart graphics / team slide / a variety of text slides / a testimonial slide / Example project slide / Final contact and Disclaimer text slide etc all customised to the design. We rely on your experience for providing the further standard formats and layouts that one might find in a high-quality financial sector corporate presentation deck.

VERSIONS: We want three versions of the slides where there are images (eg front and back covers, section breaks, testimonial slides..). The three could be themed eg (1) futuristic and/or abstract in the theme of our investment scope (2) Street themes with vehicles and people in developed and developing markets (3) a mix of aerial and land-based views of roads (4) more explicit around the types of infrastructure in which we invest (vehicles of different types, charging infrastructure, solar panels on industrial and commercial roof tops etc)

LOOK & FEEL: The presentation must be sleek, dynamic if sober, with a clean feel, it should project an image of clarity and confidence, but also elicit some emotional appeal (even if it is very subtle!) ... we are in the e-mobility sector after all! We have an existing logo (attached).

We have an existing website www.dorelmont.capital (one day it will need an upgrade too!) it may serve as inspiration / allow you better to understand our activities!

SOME PICS THAT WE LIKE: for inspiration only (NON exhaustive!):

• https://www.klipvane.com/video/stock/unrecognizable-highway-traffic-head-on-bgkbvhtcmjn19iqta
• https://www.klipvane.com/video/stock/new-york-city-streets-nt1vyz3
• https://www.klipvane.com/video/stock/4k-time-lapse-of-traffic-speeding-on-a-straight-section-of-highway-during-an-evening-rush-hour-ps1llt0
• https://www.klipvane.com/video/stock/cinematic-urban-aerial-time-lapse-of-city-infrastructure-including-freeways-interstates-roads-streets-with-traffic-at-rush-hour-during-the-evening-bzjhqhqfmjbhns0h9
• https://www.klipvane.com/video/stock/charging-of-electric-car-eco-energy-transport-and-power-supply-environmentally-conscious-transportation-vehicle-plugged-in-charger-terminal-in-the-city-4k-rsl8pukqmejqpaojnn
• https://www.klipvane.com/video/stock/drone-view-of-modern-vehicle-driving-on-road-near-ploughed-field-and-wind-turbine-in-countryside-rzwqrsqvdkg85gavm

FINALLY: note the attached 'slides to include' are additonal slides that we want to be well presented (see additional detail on Slide 1 of the file)

Target Market(s)

Institutional investors (pension funds, asset managers, family offices) & the dreamer in each of us!!

Industry/Entity Type

Financial services (B2B NOT B2C)

Font styles to use
Other font styles liked:
• Calibri but can consider alternatives

Requirements
Must have
• We need all of the usual front cover slide / content slide / intermediate divider-heading slide / slides that integrate the most common tables, charts and smart graphics / team slide / a variety of text slides / a testimonial slide / Example project slide / Final contact and Disclaimer text slide etc all customised to the design. We rely on your experience for providing the further standard formats and layouts that one might find in a high-quality financial sector corporate presentation deck
Nice to have
• Would like to see any other pages that are standard in your experience! Also would like to see one version of the slides with a summary section clearly marked for each slide (with space for text) which will serve for quick reading of the presentation for key points)

```html
<!DOCTYPE html>
<html lang="en">
<head>
<meta charset="utf-8">
<title>Dorelmont Capital – Presentation</title>
<link rel="stylesheet" href="https://fonts.googleapis.com/css2?family=Open+Sans:wght@300;400;600;700&display=swap">
<style>
:root{
  --green:#6e9e3a;
  --green-dark:#283e1c;
  --green-ink:#2b4a1c;
  --grey-bg:#e8e8e8;
  --ink:#333;
  --white:#fff;
  --black:#000;
}
*{box-sizing:border-box;margin:0;padding:0}
html,body{width:1200px;height:3654px;overflow:hidden;background:var(--white)}
body{position:relative;font-family:"Open Sans",Arial,sans-serif;color:var(--white)}
.slide{position:absolute;left:99px;width:997px;height:561px;overflow:hidden}
.abs{position:absolute}
.center{left:0;right:0;text-align:center}
.wordmark{font-weight:300;font-size:72px;letter-spacing:1px;color:var(--white);line-height:1}

/* cover */
.cover{top:56px}
.cover-photo{inset:0;background:linear-gradient(170deg,#b5713c 0%,#7a5a45 35%,#4d4a47 65%,#2f3133 100%)}
.cover .wordmark{top:266px}
.cover-tagline{top:296px;font-size:29px;font-weight:700;line-height:38px;letter-spacing:.5px}

/* about */
.about{top:645px;background:var(--green-dark)}
.about-photo{left:537px;top:0;width:460px;height:561px;background:linear-gradient(180deg,#2f3f66 0%,#6a6e86 35%,#2b2f22 60%,#5a2a22 80%,#1f1f1f 100%)}
.about-box{left:56px;top:138px;width:575px;height:285px;background:var(--green);padding:22px 20px}
.about-box h2{font-size:39px;font-weight:600;line-height:48px;margin-bottom:6px}
.about-box p{font-size:15.5px;line-height:33.5px}

/* projects */
.projects{top:1238px;background:var(--green)}
.projects h2{top:32px;font-size:40px;font-weight:700}
.projects .lead{top:96px;font-size:15.5px}
.projects-photo{left:32px;top:155px;width:442px;height:347px;background:linear-gradient(160deg,#8a8f96 0%,#4e7e92 35%,#c9c27a 60%,#5f6058 100%)}
.invest{left:500px;top:146px;width:470px}
.invest h3{font-size:26px;font-weight:700;line-height:38px}
.invest .intro{font-size:15px;margin:10px 0 14px}
.ticks{list-style:none}
.ticks li{position:relative;padding-left:18px;font-size:12.6px;line-height:21px;margin-bottom:10px}
.ticks svg{position:absolute;left:0;top:5px}

/* chart */
.chart-slide{top:1831px;background:var(--grey-bg)}
.chart-slide h2{top:38px;font-size:40px;font-weight:700;color:var(--green-ink)}
.chart{left:0;top:0}
.chart text{font-family:"Open Sans",Arial,sans-serif;font-size:12px;font-weight:700;fill:var(--ink)}

/* team */
.team{top:2426px}
.team-photo{inset:0;background:linear-gradient(120deg,#2e4a1e 0%,#3f5f28 40%,#34501f 70%,#24391a 100%)}
.team h2{top:44px;font-size:40px;font-weight:700}
.team .lead{top:108px;font-size:17.5px;line-height:32px}
.card{top:233px;width:208px;height:274px;background:var(--white);text-align:center;color:var(--ink)}
.card .portrait{width:127px;height:127px;border-radius:50%;margin:22px auto 0}
.card h4{margin-top:12px;font-size:17px;font-weight:700;color:var(--green-ink)}
.card .role{font-size:13px;font-weight:600;color:var(--green);line-height:18px}
.card p{font-size:9.5px;line-height:18px;margin-top:3px;padding:0 12px}

/* thanks */
.thanks{top:3023px}
.thanks-photo{inset:0;background:linear-gradient(180deg,#6f5a3c 0%,#4a3b2e 40%,#2f2b2b 75%,#1c1c1f 100%)}
.thanks h2{top:110px;font-size:42px;font-weight:700}
.thanks .lead{top:176px;font-size:17.5px;line-height:32px}
.thanks .wordmark{top:281px}
.contact{top:381px;display:flex;align-items:center;gap:12px;font-size:13.5px;line-height:21px}
.contact .icon{width:54px;height:54px;border-radius:50%;background:var(--green);border:2px solid var(--white);display:flex;align-items:center;justify-content:center;flex:none}
</style>
</head>
<body>

<section class="slide cover">
  <div class="abs cover-photo" role="img" aria-label="Motion-blurred highway traffic at sunset"></div>
  <div class="abs center wordmark">Dorelmont Capital</div>
  <p class="abs center cover-tagline" style="top:296px;margin-top:55px">Project finance to scale electric<br>vehicles, globally</p>
</section>

<section class="slide about">
  <div class="abs about-photo" role="img" aria-label="Time-lapse light trails on a motorway at dusk"></div>
  <div class="abs about-box">
    <h2>About Dorelmont Capital</h2>
    <p>Dorelmont Capital S.A. is a yet-to-be established investment advisory and management company. The company was founded in early 2020 in recognition of the growing need for, and opportunity that lies within, sustainable transport. Dorelmont Capital was selected for the Spring 2020 cohort of the Greenway Climate Accelerator programme.</p>
  </div>
</section>

<section class="slide projects">
  <h2 class="abs center">Projects</h2>
  <p class="abs center lead">We provide project financing to enable owners and operators of commercial fleets to adopt cleaner technologies.</p>
  <div class="abs projects-photo" role="img" aria-label="Busy city bus terminal with commuters"></div>
  <div class="abs invest">
    <h3>What types of projects do<br>we invest in?</h3>
    <p class="intro">We invest in projects with the following characteristics:</p>
    <ul class="ticks">
      <li><svg width="12" height="12" viewBox="0 0 12 12"><circle cx="6" cy="6" r="5.2" fill="none" stroke="#fff" stroke-width="1"/><path d="M3.5 6.2l1.7 1.7 3.3-3.5" fill="none" stroke="#fff" stroke-width="1.1"/></svg>The project enables owners and operators of commercial fleets (such as buses, trucks, taxis) to reduce or avoid emissions by the adoption of cleaner technologies. This could include the purchase of plug-in electric or hydrogen vehicles, the retrofitting of existing vehicles, and the installation of charging infrastructure</li>
      <li><svg width="12" height="12" viewBox="0 0 12 12"><circle cx="6" cy="6" r="5.2" fill="none" stroke="#fff" stroke-width="1"/><path d="M3.5 6.2l1.7 1.7 3.3-3.5" fill="none" stroke="#fff" stroke-width="1.1"/></svg>The project has a high climate and health impact potential, and a measurable impact at city and regional levels</li>
      <li><svg width="12" height="12" viewBox="0 0 12 12"><circle cx="6" cy="6" r="5.2" fill="none" stroke="#fff" stroke-width="1"/><path d="M3.5 6.2l1.7 1.7 3.3-3.5" fill="none" stroke="#fff" stroke-width="1.1"/></svg>The project aligns with our investment principles, and our environmental management systems</li>
      <li><svg width="12" height="12" viewBox="0 0 12 12"><circle cx="6" cy="6" r="5.2" fill="none" stroke="#fff" stroke-width="1"/><path d="M3.5 6.2l1.7 1.7 3.3-3.5" fill="none" stroke="#fff" stroke-width="1.1"/></svg>The project is expected to provide attractive financial return</li>
    </ul>
  </div>
</section>

<section class="slide chart-slide">
  <h2 class="abs center">Nemo enim ipsam voluptatem</h2>
  <svg class="abs chart" width="997" height="561" viewBox="0 0 997 561" role="img" aria-label="Bar chart of yearly values 2012 to 2021">
    <g stroke="#c4c4c4" stroke-width="1">
      <line x1="188" y1="134" x2="849" y2="134"/><line x1="188" y1="170" x2="849" y2="170"/>
      <line x1="188" y1="207" x2="849" y2="207"/><line x1="188" y1="243" x2="849" y2="243"/>
      <line x1="188" y1="279" x2="849" y2="279"/><line x1="188" y1="315" x2="849" y2="315"/>
      <line x1="188" y1="351" x2="849" y2="351"/><line x1="188" y1="387" x2="849" y2="387"/>
      <line x1="188" y1="424" x2="849" y2="424"/><line x1="188" y1="460" x2="849" y2="460"/>
    </g>
    <g text-anchor="end">
      <text x="178" y="138">800</text><text x="178" y="174">600</text><text x="178" y="211">400</text>
      <text x="178" y="247">200</text><text x="178" y="283">100</text><text x="178" y="319">80</text>
      <text x="178" y="355">60</text><text x="178" y="391">40</text><text x="178" y="428">20</text>
      <text x="178" y="464">0</text>
    </g>
    <g>
      <rect x="193" y="445" width="26" height="15" fill="var(--green)"/>
      <rect x="262" y="279" width="26" height="181" fill="var(--green)"/>
      <rect x="332" y="138" width="26" height="322" fill="var(--black)"/>
      <rect x="401" y="279" width="26" height="181" fill="var(--green)"/>
      <rect x="471" y="243" width="26" height="217" fill="var(--black)"/>
      <rect x="540" y="243" width="26" height="217" fill="var(--green)"/>
      <rect x="609" y="154" width="26" height="306" fill="var(--black)"/>
      <rect x="680" y="243" width="26" height="217" fill="var(--green)"/>
      <rect x="749" y="207" width="26" height="253" fill="var(--black)"/>
      <rect x="820" y="263" width="26" height="197" fill="var(--green)"/>
    </g>
    <g text-anchor="middle">
      <text x="206" y="487">2012</text><text x="275" y="487">2013</text><text x="345" y="487">2014</text>
      <text x="414" y="487">2015</text><text x="484" y="487">2016</text><text x="553" y="487">2017</text>
      <text x="622" y="487">2018</text><text x="693" y="487">2019</text><text x="762" y="487">2020</text>
      <text x="833" y="487">2021</text>
    </g>
  </svg>
</section>

<section class="slide team">
  <div class="abs team-photo" role="img" aria-label="Business team in a meeting, green-tinted"></div>
  <h2 class="abs center">Our Team</h2>
  <p class="abs center lead">Sed ut perspiciatis unde omnis iste natus error sit voluptatem accusantium doloremque laudantium,<br>totam rem aperiam, eaque ipsa quae ab illo inventore veritatis et quasi architecto<br>beatae vitae dicta sunt explicabo</p>
  <div class="abs card" style="left:41px">
    <div class="portrait" role="img" aria-label="Portrait photo of team member" style="background:#3a3f48"></div>
    <h4>Arlo Pennick</h4><div class="role">Partner</div>
    <p>Sed ut perspiciatis unde omnis iste natus error sit voluptatem accusantium dolo enim ipsam voluptatem quia.</p>
  </div>
  <div class="abs card" style="left:277px">
    <div class="portrait" role="img" aria-label="Portrait photo of team member" style="background:#55627a"></div>
    <h4>Kenji Murase</h4><div class="role">Partner</div>
    <p>Sed ut perspiciatis unde omnis iste natus error sit voluptatem accusantium dolo enim ipsam voluptatem quia.</p>
  </div>
  <div class="abs card" style="left:513px">
    <div class="portrait" role="img" aria-label="Portrait photo of team member" style="background:#2f2c2a"></div>
    <h4>Darius Halvorsen</h4><div class="role">Partner</div>
    <p>Sed ut perspiciatis unde omnis iste natus error sit voluptatem accusantium dolo enim ipsam voluptatem quia.</p>
  </div>
  <div class="abs card" style="left:749px">
    <div class="portrait" role="img" aria-label="Portrait photo of team member" style="background:#cfc6b8"></div>
    <h4>Lena Marchetti</h4><div class="role">Consultant</div>
    <p>Sed ut perspiciatis unde omnis iste natus error sit voluptatem accusantium dolo enim ipsam voluptatem quia.</p>
  </div>
</section>

<section class="slide thanks">
  <div class="abs thanks-photo" role="img" aria-label="City street with blurred traffic at dusk"></div>
  <h2 class="abs center">Thank You!</h2>
  <p class="abs center lead">Sed ut perspiciatis unde omnis iste natus error sit voluptatem accusantium doloremque laudantium,<br>totam rem aperiam, eaque ipsa quae ab illo inventore.</p>
  <div class="abs center wordmark">Dorelmont Capital</div>
  <div class="abs contact" style="left:161px">
    <span class="icon"><svg width="22" height="26" viewBox="0 0 22 26"><path d="M11 1C5.8 1 2 4.9 2 9.8 2 16 11 25 11 25s9-9 9-15.2C20 4.9 16.2 1 11 1z" fill="#fff"/><circle cx="11" cy="10" r="3.4" fill="var(--green)"/></svg></span>
    <span>Sed ut perspiciatis unde<br>omnis iste natus</span>
  </div>
  <div class="abs contact" style="left:405px">
    <span class="icon"><svg width="24" height="24" viewBox="0 0 24 24"><path d="M6.5 3.5l3 3.2-1.8 2.4c1.2 2.6 3.4 4.8 6.1 6.1l2.4-1.8 3.2 3-2 2.6C11 18.6 5.4 13 4 5.5z" fill="#fff"/></svg></span>
    <span>1-800-555-0142</span>
  </div>
  <div class="abs contact" style="left:597px">
    <span class="icon"><svg width="24" height="18" viewBox="0 0 24 18"><rect x="1" y="1" width="22" height="16" rx="2" fill="#fff"/><path d="M2 2l10 8 10-8" fill="none" stroke="var(--green)" stroke-width="1.6"/></svg></span>
    <span>hello@dorelmont.capital</span>
  </div>
</section>

</body>
</html>
```